Business Card and Simple Logo Desgin

New Zealand based start up company "Brook Advisory LTD" requires business cards and simple logo design.

Card Content.

Brook Advisory LTD

Joanna Pritchard
CA, BMS (Hons)

j.pritchard@brookadvisory.co.nz
PH +64 21 574 160

Target Market(s)

Corporate Business in IT, Finance and accounting.

Industry/Entity Type

Business

```html
<!DOCTYPE html>
<html lang="en">
<head>
<meta charset="utf-8">
<title>Brook Advisory LTD – Business Card</title>
<link href="https://fonts.googleapis.com/css2?family=Mulish:wght@400;500&display=swap" rel="stylesheet">
<style>
  :root {
    --page-bg: #ffffff;
    --card-bg: #f3f3f3;
    --brand-green: #00b140;
    --ink: #1a1a1a;
  }
  html, body {
    margin: 0;
    padding: 0;
    width: 900px;
    height: 1200px;
    overflow: hidden;
    background: var(--page-bg);
    font-family: "Mulish", "Helvetica Neue", Arial, sans-serif;
    color: var(--ink);
  }
  .canvas {
    position: relative;
    width: 900px;
    height: 1200px;
  }
  .card {
    position: absolute;
    left: 152px;
    top: 105px;
    width: 576px;
    height: 1008px;
    background: var(--card-bg);
  }
  .brand {
    position: absolute;
    left: 66px;
    top: 240px;
  }
  .brand-mark {
    display: flex;
    align-items: center;
    gap: 20px;
    height: 102px;
  }
  .brand-square {
    width: 64px;
    height: 64px;
    background: var(--brand-green);
    flex: none;
  }
  .brand-name {
    margin: 0;
    font-size: 64px;
    font-weight: 500;
    line-height: 1;
    color: var(--ink);
  }
  .brand-company {
    margin: 12px 0 0 0;
    font-size: 29px;
    font-weight: 400;
    letter-spacing: 1px;
    line-height: 1;
    text-transform: uppercase;
    white-space: nowrap;
  }
  .contact {
    position: absolute;
    left: 54px;
    top: 700px;
    font-style: normal;
  }
  .contact p { margin: 0; }
  .contact-name {
    font-size: 32px;
    font-weight: 500;
    line-height: 1.2;
  }
  .contact-credentials {
    margin-top: 2px !important;
    font-size: 19px;
    font-weight: 400;
  }
  .contact-email {
    margin-top: 12px !important;
    font-size: 31px;
    font-weight: 400;
    white-space: nowrap;
  }
  .contact-phone {
    margin-top: 0 !important;
    font-size: 31px;
    font-weight: 400;
  }
  .contact-phone-label {
    font-size: 18px;
    margin-right: 10px;
  }
</style>
</head>
<body>
  <main class="canvas">
    <section class="card" aria-label="Business card">
      <header class="brand">
        <div class="brand-mark">
          <span class="brand-square" aria-hidden="true"></span>
          <p class="brand-name">Brook</p>
        </div>
        <p class="brand-company">Brook Advisory LTD</p>
      </header>
      <address class="contact">
        <p class="contact-name">Joanna Pritchard</p>
        <p class="contact-credentials">CA, BMS (Hons)</p>
        <p class="contact-email">j.pritchard@brookadvisory.co.nz</p>
        <p class="contact-phone"><span class="contact-phone-label">Tel</span>+64 21 574 160</p>
      </address>
    </section>
  </main>
</body>
</html>
```